Design some Business Cards Education Consultancy

Make a Brand Stationary Design for us.. in Adobe illustrator or CoralDraw

First step Design Business Card with your Innovative Themes,

Put Original data form attached file.lke name , address , mob ,email.etc.. don't show me in dummy data.

Before winning , we will take other design like Letter Head , Envelop , ID Card.

Only Vector File Accepting... PSD file will reject

Check Detail In attachment file.

```html
<!DOCTYPE html>
<html lang="en">
<head>
<meta charset="utf-8">
<title>Bright Path Admissions – Business Card</title>
<link href="https://fonts.googleapis.com/css2?family=Open+Sans:wght@400;600;700;800&display=swap" rel="stylesheet">
<style>
  :root {
    --bg: #e6e9ed;
    --card: #ffffff;
    --cyan: #1fb1e0;
    --cyan-soft: #7fd3ef;
    --navy: #2a3990;
    --ink: #333a44;
    --grey: #6b717a;
    --orange: #f39a1f;
  }
  * { box-sizing: border-box; margin: 0; padding: 0; }
  html, body { width: 1200px; height: 900px; overflow: hidden; }
  body {
    background: var(--bg);
    font-family: "Open Sans", Arial, sans-serif;
    color: var(--ink);
    position: relative;
  }
  .card {
    position: absolute;
    width: 640px;
    height: 366px;
    background: var(--card);
    border-radius: 22px;
    overflow: hidden;
    box-shadow: 0 6px 18px rgba(0,0,0,0.12);
  }
  .card--back { left: 280px; top: 50px; }
  .card--front { left: 280px; top: 484px; }

  .brand-mark {
    position: absolute;
    width: 86px; height: 86px;
    border-radius: 50%;
    background: var(--cyan);
  }
  .brand-name {
    position: absolute;
    font-weight: 800;
    color: var(--navy);
    text-transform: uppercase;
    letter-spacing: 0.5px;
    white-space: nowrap;
  }
  .tagline {
    position: absolute;
    font-weight: 400;
    color: var(--grey);
    white-space: nowrap;
  }

  .card--back .brand-mark { left: 272px; top: 58px; width: 96px; height: 96px; }
  .card--back .brand-name { left: 0; right: 0; top: 170px; text-align: center; font-size: 22px; }
  .card--back .tagline { left: 0; right: 0; top: 204px; text-align: center; font-size: 18px; }
  .web-pill {
    position: absolute;
    left: 88px; top: 262px;
    width: 270px; height: 36px;
    border-radius: 18px;
    background: var(--cyan);
    color: #fff;
    font-size: 14px;
    font-weight: 600;
    display: flex; align-items: center; justify-content: center;
  }

  .bunting {
    position: absolute;
    left: 70px; top: 0;
    width: 180px; height: 52px;
    background: linear-gradient(90deg, var(--orange), #f7b54a 45%, #3a6fc4);
    clip-path: polygon(0 0, 100% 0, 100% 100%, 0 60%);
  }
  .card--front .brand-mark { left: 108px; top: 72px; }
  .card--front .brand-name { left: 34px; top: 170px; width: 212px; text-align: center; font-size: 15px; }
  .card--front .tagline { left: 34px; top: 196px; width: 212px; text-align: center; font-size: 14px; }

  .contact {
    position: absolute;
    left: 330px; top: 80px;
    width: 290px;
  }
  .contact__name { font-size: 26px; font-weight: 800; color: var(--navy); line-height: 1.05; }
  .contact__role { font-size: 12px; color: var(--grey); margin-bottom: 10px; }
  .contact__company { font-size: 16px; font-weight: 800; color: var(--navy); text-transform: uppercase; }
  .contact__address { font-size: 11.5px; line-height: 1.4; margin-bottom: 8px; }
  .contact__line {
    display: flex; align-items: center; gap: 8px;
    font-size: 14px; line-height: 1.5;
  }
  .contact__line svg { width: 14px; height: 14px; flex: none; }

  .band { position: absolute; left: 0; top: 0; width: 640px; height: 366px; }
  .service {
    position: absolute;
    left: 26px; top: 296px;
    font-size: 13.5px;
    font-weight: 600;
    color: var(--ink);
    white-space: nowrap;
  }
</style>
</head>
<body>

  <section class="card card--back" aria-label="Business card back">
    <div class="brand-mark"></div>
    <div class="brand-name">Bright Path Admissions</div>
    <div class="tagline">Guiding Your Tomorrow</div>
    <div class="web-pill">www.brightpathadmissions.com</div>
  </section>

  <section class="card card--front" aria-label="Business card front">
    <svg class="band" viewBox="0 0 640 366" aria-hidden="true">
      <path d="M0 258 H150 Q172 258 178 280" fill="none" stroke="var(--cyan)" stroke-width="6"/>
      <path d="M0 336 H640 V366 H0 Z" fill="var(--cyan)"/>
      <path d="M0 326 H640 V334 H0 Z" fill="var(--cyan-soft)"/>
    </svg>

    <div class="bunting" role="img" aria-label="Orange and blue pennant bunting decoration"></div>

    <div class="brand-mark"></div>
    <div class="brand-name">Bright Path Admissions</div>
    <div class="tagline">Guiding Your Tomorrow</div>

    <div class="contact">
      <div class="contact__name">ROHAN MEHTA</div>
      <div class="contact__role">Director</div>
      <div class="contact__company">Bright Path Admissions</div>
      <div class="contact__address">
        Lakeview Plaza, Office 412, S.NO 118 BANER,<br>
        OPP CITY GARDEN HOTEL BANER<br>
        Pin code: 411045
      </div>
      <div class="contact__line">
        <svg viewBox="0 0 16 16"><path d="M4 1.5 L6.5 4.5 L5 6.5 Q6.5 9.5 9.5 11 L11.5 9.5 L14.5 12 L13 14.5 Q7 15 3 9 Q1 5 4 1.5 Z" fill="var(--navy)"/></svg>
        <span>7300145260</span>
      </div>
      <div class="contact__line">
        <svg viewBox="0 0 16 16"><rect x="1" y="3" width="14" height="10" fill="none" stroke="var(--navy)" stroke-width="1.6"/><path d="M1 3 L8 9 L15 3" fill="none" stroke="var(--navy)" stroke-width="1.6"/></svg>
        <span>hello@brightpathadmissions.com</span>
      </div>
      <div class="contact__line">
        <svg viewBox="0 0 16 16"><circle cx="8" cy="8" r="6.5" fill="none" stroke="var(--cyan)" stroke-width="1.5"/><ellipse cx="8" cy="8" rx="3" ry="6.5" fill="none" stroke="var(--cyan)" stroke-width="1.2"/><path d="M1.5 8 H14.5" stroke="var(--cyan)" stroke-width="1.2"/></svg>
        <span>www.brightpathadmissions.com</span>
      </div>
    </div>

    <div class="service">EDUCATIONAL ADMISSION CONSULTANCY OVER ALL INDIA</div>
  </section>

</body>
</html>
```